Hair salon and Nail salon in Hawaii need a newspaper Ad design.

We need a newspaper Ad design for new open hair & nail salon in Waikiki Hawaii.Our Recommendation service for hair is "Head Spa" $30+tax and for nail is "Manicure Treatment Course" (Filing+Cuticle Care+Massage+Coloring) $20+tax.
We would like to see Hawaiian taste color and also having sense of luxury design. The ad size is W 5.0” x H 6.375”.
I would customers to know the shop place(Lanakila Crest Hotel 1F) , phone(808-555-0173), instagram(salonbrightwave) , our web site https://salonbrightwave.example and recommend services. For Web or Instagram , QR code is acceptable.

Target Market(s)

women & men

Industry/Entity Type

Beauty Salon

Font styles to use
Serif

Colors

Designer to choose colors to be used in the design.

Requirements
Must have
• Tagline for local customers. Shop Name is "SALON BRIGHTWAVE".the shop place(Lanakila Crest Hotel 1F) , phone(808-555-0173), instagram(salonbrightwave) and recommend services.
Nice to have
• Our services are competitive, but we don't want to be seen as just cheap and low quality.

```html
<!DOCTYPE html>
<html lang="en">
<head>
<meta charset="utf-8">
<title>Salon Brightwave – Newspaper Ad</title>
<link rel="stylesheet" href="https://fonts.googleapis.com/css2?family=Alfa+Slab+One&family=Bodoni+Moda:wght@500&family=Roboto+Slab:wght@400;800;900&family=Tinos:wght@400;700&family=Ubuntu:wght@400&display=swap">
<style>
  :root {
    --ink: #0b0303;
    --deep-red: #3a0706;
    --wine: #6b0f0c;
    --maroon-text: #7a1210;
    --rust: #a3301a;
    --glow-orange: #f28a12;
    --glow-yellow: #ffe36a;
    --gold-top: #ffd23a;
    --gold-bottom: #f07a10;
    --white: #ffffff;
    --band-dark: rgba(40, 4, 4, 0.78);
    --teal-text: #9fe3ee;
  }
  html, body {
    margin: 0;
    padding: 0;
    overflow: hidden;
    background: var(--ink);
  }
  .ad {
    position: relative;
    width: 1200px;
    height: 940px;
    overflow: hidden;
    background:
      radial-gradient(ellipse 60% 45% at 72% 55%, var(--wine) 0%, transparent 75%),
      linear-gradient(180deg, var(--ink) 0%, #1a0303 18%, var(--deep-red) 40%, var(--wine) 62%, #2a0504 82%, var(--ink) 100%);
    font-family: "Tinos", serif;
  }
  .portrait {
    position: absolute;
    left: 0; top: 0;
    width: 540px; height: 940px;
    background:
      radial-gradient(ellipse 40% 30% at 20% 22%, #c9853a 0%, transparent 70%),
      radial-gradient(ellipse 55% 70% at 30% 60%, #8a2a14 0%, transparent 75%),
      linear-gradient(90deg, #5a1208 0%, #7a1e0e 45%, #3a0806 85%, transparent 100%);
  }
  .glow-band {
    position: absolute;
    right: 0;
    background:
      linear-gradient(90deg, transparent 0%, rgba(242,138,18,0.6) 12%, var(--glow-yellow) 28%, var(--glow-orange) 70%, rgba(242,138,18,0.5) 100%);
    -webkit-mask: linear-gradient(180deg, transparent 0%, #000 35%, #000 65%, transparent 100%);
            mask: linear-gradient(180deg, transparent 0%, #000 35%, #000 65%, transparent 100%);
  }
  .glow-band--spa { top: 210px; height: 76px; width: 740px; }
  .glow-band--manicure { top: 440px; height: 80px; width: 740px; }

  .brand-mark {
    position: absolute;
    left: 464px; top: 28px;
    width: 125px; height: 134px;
    background: #5e6b66;
    border: 3px solid #1c1c1c;
    box-shadow: 0 0 10px rgba(255,255,255,0.7);
  }
  .brand-name {
    position: absolute;
    left: 610px; top: 30px;
    width: 540px;
    margin: 0;
    text-align: center;
    font-family: "Tinos", serif;
    font-weight: 700;
    font-size: 68px;
    line-height: 70px;
    letter-spacing: 1px;
    background: linear-gradient(180deg, var(--gold-top) 0%, var(--gold-bottom) 100%);
    -webkit-background-clip: text;
            background-clip: text;
    color: transparent;
  }
  .service-title {
    position: absolute;
    left: 540px; width: 650px;
    margin: 0;
    text-align: center;
    font-family: "Roboto Slab", serif;
    font-weight: 900;
    color: var(--maroon-text);
    -webkit-text-stroke: 7px var(--white);
    paint-order: stroke fill;
    text-transform: uppercase;
  }
  .service-title--spa { top: 225px; font-size: 56px; line-height: 60px; letter-spacing: 1px; }
  .service-title--manicure { top: 454px; font-size: 38px; line-height: 38px; letter-spacing: 0.5px; }

  .price-burst {
    position: absolute;
    left: 708px;
    width: 314px; height: 96px;
  }
  .price-burst svg { position: absolute; inset: 0; width: 100%; height: 100%; filter: drop-shadow(0 2px 4px rgba(0,0,0,0.5)); }
  .price-burst span {
    position: absolute; inset: 0;
    display: flex; align-items: center; justify-content: center;
    font-family: "Alfa Slab One", serif;
    font-size: 40px;
    color: var(--maroon-text);
  }
  .price-burst--spa { top: 323px; }
  .price-burst--manicure { top: 613px; }

  .info-band {
    position: absolute;
    right: 0;
    background: var(--band-dark);
    color: var(--white);
    display: flex; align-items: center;
  }
  .info-band--steps {
    top: 549px; width: 648px; height: 38px;
    justify-content: center;
    font-family: "Roboto Slab", serif;
    font-size: 27px;
    letter-spacing: 0.5px;
  }
  .info-band--location {
    top: 742px; width: 610px; height: 48px;
    padding-left: 20px; box-sizing: border-box;
    font-family: "Ubuntu", sans-serif;
    font-size: 30px;
    gap: 8px;
  }
  .info-band--location svg { width: 30px; height: 36px; }

  .phone {
    position: absolute;
    left: 560px; top: 786px; width: 580px;
    margin: 0;
    text-align: center;
    font-family: "Bodoni Moda", serif;
    font-weight: 500;
    font-size: 92px;
    line-height: 100px;
    color: var(--white);
    letter-spacing: 1px;
  }
  .links {
    position: absolute;
    left: 520px; top: 884px;
    display: flex; align-items: center;
    gap: 10px;
    font-family: "Tinos", serif;
    font-size: 22px;
    color: var(--teal-text);
  }
  .links .social-square {
    width: 28px; height: 28px;
    background: #c8388a;
    border-radius: 4px;
  }
  .links .divider {
    width: 2px; height: 34px;
    background: var(--white);
    margin: 0 8px;
  }
  .links svg { width: 26px; height: 26px; }
</style>
</head>
<body>
<div class="ad">
  <div class="portrait" role="img" aria-label="Photo of a woman in profile with long glossy red-auburn hair and bangs"></div>

  <div class="glow-band glow-band--spa"></div>
  <div class="glow-band glow-band--manicure"></div>

  <div class="brand-mark"></div>
  <h1 class="brand-name">SALON<br>BRIGHTWAVE</h1>

  <h2 class="service-title service-title--spa">Head Spa</h2>
  <div class="price-burst price-burst--spa">
    <svg viewBox="-100 -30 200 60" preserveAspectRatio="none" aria-hidden="true">
      <polygon fill="#ffffff" points="100,0 79,3.7 95,9.3 71.3,10.9 80.9,17.6 56.6,17 58.8,24.3 36.3,21.4 30.9,28.5 12.5,23.7 0,30 -12.5,23.7 -30.9,28.5 -36.3,21.4 -58.8,24.3 -56.6,17 -80.9,17.6 -71.3,10.9 -95,9.3 -79,3.7 -100,0 -79,-3.7 -95,-9.3 -71.3,-10.9 -80.9,-17.6 -56.6,-17 -58.8,-24.3 -36.3,-21.4 -30.9,-28.5 -12.5,-23.7 0,-30 12.5,-23.7 30.9,-28.5 36.3,-21.4 58.8,-24.3 56.6,-17 80.9,-17.6 71.3,-10.9 95,-9.3 79,-3.7"/>
    </svg>
    <span>$30+Tax.</span>
  </div>

  <h2 class="service-title service-title--manicure">Manicure Treatment<br>Course</h2>
  <div class="info-band info-band--steps">(Filing+Cuticle Care+Massage+Coloring)</div>
  <div class="price-burst price-burst--manicure">
    <svg viewBox="-100 -30 200 60" preserveAspectRatio="none" aria-hidden="true">
      <polygon fill="#ffffff" points="100,0 79,3.7 95,9.3 71.3,10.9 80.9,17.6 56.6,17 58.8,24.3 36.3,21.4 30.9,28.5 12.5,23.7 0,30 -12.5,23.7 -30.9,28.5 -36.3,21.4 -58.8,24.3 -56.6,17 -80.9,17.6 -71.3,10.9 -95,9.3 -79,3.7 -100,0 -79,-3.7 -95,-9.3 -71.3,-10.9 -80.9,-17.6 -56.6,-17 -58.8,-24.3 -36.3,-21.4 -30.9,-28.5 -12.5,-23.7 0,-30 12.5,-23.7 30.9,-28.5 36.3,-21.4 58.8,-24.3 56.6,-17 80.9,-17.6 71.3,-10.9 95,-9.3 79,-3.7"/>
    </svg>
    <span>$20+Tax.</span>
  </div>

  <div class="info-band info-band--location">
    <svg viewBox="0 0 24 30" aria-hidden="true">
      <path d="M12 1.5C6.5 1.5 2.5 5.6 2.5 10.8 2.5 18 12 28.5 12 28.5S21.5 18 21.5 10.8C21.5 5.6 17.5 1.5 12 1.5Z" fill="none" stroke="#ffffff" stroke-width="2.4"/>
      <circle cx="12" cy="10.8" r="3.6" fill="none" stroke="#ffffff" stroke-width="2.2"/>
    </svg>
    <span>Lanakila Crest Hotel 1F.</span>
  </div>

  <p class="phone">808-555-0173</p>

  <div class="links">
    <span class="social-square"></span>
    <span>salonbrightwave</span>
    <span class="divider"></span>
    <svg viewBox="0 0 24 24" aria-hidden="true" fill="none" stroke="#ffffff" stroke-width="1.6">
      <circle cx="12" cy="12" r="10"/>
      <ellipse cx="12" cy="12" rx="4.5" ry="10"/>
      <line x1="2" y1="12" x2="22" y2="12"/>
      <path d="M4 7h16M4 17h16"/>
    </svg>
    <span>www.salonbrightwave.example</span>
  </div>
</div>
</body>
</html>
```